Banner for homepage

It is a new banner for the homepage, temporary site address is 61.187.40.72 ( is the biggest banner only ) . Would be 5 variations for image content as below (in Portuguese ) :

Image 1:
Leitor de codigo de barras
Todos os tipos de leitores de código de barras para as mais diversas aplicações.
( example of product images in : http://www.quentorlabs.com/en-US/Pages/Category.aspx?category=barcode-scanners&cat=KLT)

Image 2:
Impressora de etiquetas
Identifique o que for nessário com o melhor custo/beneficio e flexibilidade de materiais de impressão.
( example of product images in : vintor.com in label printers desktop and industrial)

Image 3:
Impressora de cupom
Imprima recibos e cupons fiscais com agilidade e qualidade, temos a impressora certa para o seu PDV.
( example of product images in : http://www.palutrek.com.br/equipamento-categoria-impressoras+fiscais.html)

Image 4:
Coletor de dados
Computadores móveis com leitor de código de barras, que levam a automação para frente de trabalho.
( example of product images in : http://www.quentorlabs.com/en-US/Pages/Category.aspx?cat=KLT&category=hand-held-mobile-computer)

Image 5:
Etiquetas e Ribbons:
Etiquetas adesivas e não adesivas em vários de tipos de materiais, papéis e plásticos. O ribbon certo para impressão perfeita em cada material.
( example of product images in : http://www.tagmirelo.com/cats/supplies/barcode-printer.htm?nav=hdr)

```html
<!DOCTYPE html>
<html lang="pt-BR">
<head>
<meta charset="utf-8">
<title>Impressora de cupom</title>
<link rel="stylesheet" href="https://fonts.googleapis.com/css2?family=Jost:wght@400;500;700&display=swap">
<style>
  :root {
    --bg-center: #f7f7f7;
    --bg-edge: #dcdcdc;
    --title: #151515;
    --body: #858585;
    --button-bg: #1c1c1c;
    --button-text: #ffffff;
    --product-dark: #2b2d30;
    --product-mid: #4a4d52;
  }
  html, body {
    margin: 0;
    padding: 0;
    width: 1200px;
    height: 549px;
    overflow: hidden;
  }
  .banner {
    position: relative;
    width: 1200px;
    height: 549px;
    background: radial-gradient(ellipse 75% 90% at 55% 45%, var(--bg-center) 0%, #ececec 60%, var(--bg-edge) 100%);
    font-family: "Jost", sans-serif;
  }
  .banner__product {
    position: absolute;
    left: 92px;
    top: 148px;
    width: 300px;
    height: 350px;
    border-radius: 30px 30px 18px 18px;
    background: linear-gradient(160deg, var(--product-mid) 0%, var(--product-dark) 70%);
  }
  .banner__title {
    position: absolute;
    left: 470px;
    top: 138px;
    margin: 0;
    font-weight: 400;
    font-size: 50px;
    line-height: 1;
    color: var(--title);
    letter-spacing: 0.5px;
  }
  .banner__text {
    position: absolute;
    left: 471px;
    top: 215px;
    width: 680px;
    margin: 0;
    font-weight: 500;
    font-size: 25px;
    line-height: 31px;
    letter-spacing: 1.4px;
    color: var(--body);
  }
  .banner__cta {
    position: absolute;
    left: 471px;
    top: 350px;
    width: 161px;
    height: 41px;
    display: flex;
    align-items: center;
    justify-content: center;
    gap: 10px;
    background: var(--button-bg);
    color: var(--button-text);
    font-weight: 700;
    font-size: 18px;
    letter-spacing: 1px;
    text-decoration: none;
  }
  .banner__cta svg { display: block; }
</style>
</head>
<body>
  <section class="banner">
    <div class="banner__product" role="img" aria-label="Impressora térmica de cupom fiscal preta"></div>
    <h1 class="banner__title">Impressora de cupom</h1>
    <p class="banner__text">Imprima recibos e cupons fiscais com<br>agilidade e qualidade, temos a impressora<br>certa para o seu PDV.</p>
    <a class="banner__cta" href="#">VEJA MAIS
      <svg width="9" height="14" viewBox="0 0 9 14" aria-hidden="true"><path d="M1.5 1.5 L7 7 L1.5 12.5" fill="none" stroke="currentColor" stroke-width="2.6"/></svg>
    </a>
  </section>
</body>
</html>
```